Civic Shieldwell Company

We have design at www.brivatrust.com and want
New site design
Carallax
Images added
Were looking for your eyes. Just placement and look and feel. No hard coding. Design only.

It Company

```html
<!DOCTYPE html>
<html lang="en">
<head>
<meta charset="utf-8">
<title>Brivatrust – Protect Your Identity</title>
<link href="https://fonts.googleapis.com/css2?family=Roboto:ital,wght@0,300;0,400;0,500;0,700;1,500&family=Roboto+Slab:wght@300;400;700&display=swap" rel="stylesheet">
<style>
  :root {
    --black: #000000;
    --red: #ff0000;
    --coral: #f7837e;
    --text: #1a1a1a;
    --muted: #333333;
    --section-bg: #f2f2f2;
    --white: #ffffff;
  }
  * { margin: 0; padding: 0; box-sizing: border-box; }
  html, body { width: 1024px; height: 1200px; overflow: hidden; }
  body { position: relative; font-family: "Roboto", sans-serif; background: var(--section-bg); color: var(--text); }

  .site-header { position: absolute; top: 0; left: 0; width: 1024px; height: 55px; background: var(--black); }
  .brand { position: absolute; left: 128px; top: 13px; font-family: "Roboto Slab", serif; font-weight: 700; font-size: 24px; color: var(--white); letter-spacing: 0.5px; }
  .signin { position: absolute; left: 700px; top: 20px; display: flex; align-items: center; gap: 5px; color: var(--white); font-size: 9px; font-weight: 500; }
  .cta-header { position: absolute; left: 756px; top: 12px; width: 140px; height: 32px; background: var(--red); color: var(--white); font-weight: 700; font-size: 14px; display: flex; align-items: center; justify-content: center; }

  .hero { position: absolute; top: 55px; left: 0; width: 1024px; height: 531px;
    background: linear-gradient(100deg, #e9ece6 0%, #e8c9bf 25%, #d9b29a 45%, #a9c9a0 60%, #c9a58f 75%, #9fbf86 100%); }
  .hero-title { position: absolute; top: 295px; left: 0; width: 1024px; text-align: center; font-weight: 700; font-size: 64px; color: var(--black); letter-spacing: -0.5px; }
  .hero-button { position: absolute; left: 338px; top: 383px; width: 348px; height: 56px; background: var(--coral); display: flex; color: var(--white); }
  .hero-button .label { flex: 1; display: flex; align-items: center; justify-content: center; font-family: "Roboto Slab", serif; font-weight: 700; font-size: 17px; border-right: 1px solid rgba(255,255,255,0.6); }
  .hero-button .play { width: 56px; display: flex; align-items: center; justify-content: center; }
  .slide-nav { position: absolute; left: 995px; top: 265px; display: flex; flex-direction: column; gap: 12px; }

  .features-title { position: absolute; top: 655px; left: 0; width: 1024px; text-align: center; font-family: "Roboto Slab", serif; font-weight: 300; font-size: 50px; letter-spacing: 1px; color: var(--black); }
  .features-rule { position: absolute; top: 728px; left: 392px; width: 240px; height: 1px; background: var(--black); }

  .feature { position: absolute; width: 384px; height: 96px; }
  .feature .thumb { position: absolute; left: 0; top: 0; width: 96px; height: 96px; border-radius: 50%; }
  .feature h3 { position: absolute; left: 108px; top: 9px; font-weight: 500; font-size: 14.5px; color: var(--black); }
  .feature p { position: absolute; left: 108px; top: 29px; width: 248px; font-weight: 300; font-size: 11.2px; line-height: 16.8px; color: var(--muted); }
  .feature .more { position: absolute; right: 0; font-style: italic; font-weight: 500; font-size: 8px; color: var(--red); }

  .bottom-notch { position: absolute; left: 0; top: 1195px; width: 1024px; height: 5px; background: var(--white); }
</style>
</head>
<body>
  <header class="site-header">
    <div class="brand">Brivatrust</div>
    <div class="signin">
      <svg width="12" height="12" viewBox="0 0 12 12"><circle cx="6" cy="3.5" r="3" fill="#fff"/><path d="M0 12c0-4 3-5.5 6-5.5s6 1.5 6 5.5z" fill="#fff"/></svg>
      Signin
    </div>
    <div class="cta-header">Get Started NOW!</div>
  </header>

  <section class="hero" role="img" aria-label="Photo of a smiling family of four outdoors, children riding piggyback on their parents">
    <h1 class="hero-title">Protect Your Identity</h1>
    <div class="hero-button">
      <span class="label">Watch How We Protect You</span>
      <span class="play"><svg width="14" height="16" viewBox="0 0 14 16"><path d="M0 0L14 8L0 16z" fill="#fff"/></svg></span>
    </div>
    <div class="slide-nav">
      <svg width="12" height="10" viewBox="0 0 12 10"><path d="M0 0h12L6 10z" fill="#f7837e"/></svg>
      <svg width="12" height="10" viewBox="0 0 12 10"><path d="M0 0h12L6 10z" fill="#fff"/></svg>
      <svg width="12" height="10" viewBox="0 0 12 10"><path d="M0 0h12L6 10z" fill="#fff"/></svg>
      <svg width="12" height="10" viewBox="0 0 12 10"><path d="M0 0h12L6 10z" fill="#fff"/></svg>
      <svg width="12" height="10" viewBox="0 0 12 10"><path d="M0 0h12L6 10z" fill="#fff"/></svg>
      <svg width="12" height="10" viewBox="0 0 12 10"><path d="M0 0h12L6 10z" fill="#fff"/></svg>
    </div>
  </section>

  <h2 class="features-title">FEATURES</h2>
  <div class="features-rule"></div>

  <div class="feature" style="left:128px; top:793px;">
    <div class="thumb" role="img" aria-label="Photo of a woman working at a computer" style="background:linear-gradient(135deg,#d9d2cb,#6b5a4e);"></div>
    <h3>ID Monitoring &amp; Surveillance</h3>
    <p>Scanning engines, human intelligence gathering and mathematical algorithms find and analyze your data online.</p>
    <span class="more" style="top:83px;">Learn more »</span>
  </div>

  <div class="feature" style="left:543px; top:793px;">
    <div class="thumb" role="img" aria-label="Photo of stacks of banknotes" style="background:radial-gradient(circle,#b9bca6 0%,#e8e8e0 55%,#ffffff 75%);"></div>
    <h3>$25,000 Loss Insurance</h3>
    <p>Identity Fraud Loss and Expense Reimbursement Master Policy from Harrowgate Insurance is designed to...</p>
    <span class="more" style="top:83px;">Learn more »</span>
  </div>

  <div class="feature" style="left:128px; top:905px;">
    <div class="thumb" role="img" aria-label="Photo of hands holding an open wallet" style="background:linear-gradient(135deg,#c8a27f,#8a5d3c);"></div>
    <h3>Lost Wallet Service</h3>
    <p>Store information about the contents of your purse and wallet securely. If ever lost or stolen, you are protected.</p>
    <span class="more" style="top:83px;">Learn more »</span>
  </div>

  <div class="feature" style="left:543px; top:905px;">
    <div class="thumb" role="img" aria-label="Photo of a private envelope" style="background:linear-gradient(160deg,#e8e4de 0%,#c9a27a 45%,#b88d63 100%);"></div>
    <h3>Identity Theft Recovery</h3>
    <p>If your identity is stolen, we recover your ID for you or assist you in your recovery - your choice</p>
    <span class="more" style="top:67px;">Learn more »</span>
  </div>

  <div class="feature" style="left:128px; top:1017px;">
    <div class="thumb" role="img" aria-label="Photo of a hand writing with a pen on paper" style="background:linear-gradient(135deg,#f2e4dc,#d8c9c2);"></div>
    <h3>ID vs Credit Monitoring</h3>
    <p>Identity scoring and monitoring is more effective than credit report monitoring. Study by Fielding Group.</p>
    <span class="more" style="top:83px;">Learn more »</span>
  </div>

  <div class="feature" style="left:543px; top:1017px;">
    <div class="thumb" role="img" aria-label="Photo of a masked thief holding an identity card" style="background:linear-gradient(135deg,#2a2a2a,#111111 60%,#7d8fa3);"></div>
    <h3>Faces of ID Theft</h3>
    <p>Criminals use sophisticated methods to obtain and misuse our personal information.</p>
    <span class="more" style="top:67px;">Learn more »</span>
  </div>

  <div class="bottom-notch">
    <svg style="position:absolute; left:496px; top:-5px;" width="32" height="10" viewBox="0 0 32 10"><path d="M0 5h10l6 5 6-5h10v5H0z" fill="#ffffff"/></svg>
  </div>
</body>
</html>
```